Bottle label for a drinking or cocktail vinegar called Stone Hollow Shrub

We need a label for a square bottle that measures 2.75 inches on a side and is 6.75 inches tall. The volume is 16.9oz/500mL. The corners are rounded. A photo has been uploaded. The label should be one piece that wraps around 2-3 sides rather than separate front and back labels. The maximum height of the label can be 3.25 inches.

The company name is Stone Hollow Vinegar Works. The product line is called Stone Hollow Shrub.

The product is what is called a drinking vinegar, or sometimes cocktail vinegar, the kind of vinegar that is added to cocktails or used to make a beverage. Drinking vinegar, also known as a shrub, is vinegar and sugar mixed with fruit. The resulting elixir is tart and sweet, and is used as an alternative to lemon or lime in many drinks where it introduces an acid but with a different fruit flavor. A simple, non-alcoholic beverage can be made by adding shrub to sparkling water over ice.

Stone Hollow Shrubs are handcrafted in small batches in a small town called Deep River which is on the bank of the Connecticut River in New England. Some of the flavors include Pomegranate, Pineapple/Basil, Cherry, Fennel/Apple, and Elderberry. New flavors are added and old flavors go away, such is the nature of small batch production.

Some key words that may be useful are: artisan, small batch, handcrafted, cocktail vinegar, drinking vinegar, shrub, seasonal, natural, whole fruit.

Target Market(s)

The target audience is 25-40 year olds that drink cocktails rather than beer.

Requirements
Must have
• In addition to usual label contents (name, ingredients, volume, company info, etc.), There should be space for a hand written Batch number, description of a shrub, sample recipes, “Shake before using”.
Should not have
• nutrition labeling is not needed

```html
<!DOCTYPE html>
<html lang="en">
<head>
<meta charset="utf-8">
<title>Stone Hollow Shrub – Cocktail Vinegar Label</title>
<link href="https://fonts.googleapis.com/css2?family=Cinzel:wght@900&family=Arimo:wght@400&family=Tinos:wght@400&display=swap" rel="stylesheet">
<style>
  :root{
    --page:#ffffff;
    --label-cream:#f3efdd;
    --band:#b5b0a0;
    --band-edge:#8f8a7b;
    --ink:#1e1e1e;
    --rule:#7d7a70;
    --magenta:#c51f6b;
    --leaf:#3f8f3a;
    --fruit-deep:#8e1a24;
    --fruit-light:#d6454e;
    --brand-green:#2f7d55;
    --small-ink:#4a4843;
  }
  *{box-sizing:border-box;margin:0;padding:0}
  html,body{width:1200px;height:836px;overflow:hidden;background:var(--page)}
  .canvas{position:relative;width:1200px;height:836px}
  .label{
    position:absolute;left:110px;top:18px;width:980px;height:800px;
    background:var(--label-cream);overflow:hidden;
  }
  .border-band{
    position:absolute;left:0;width:100%;height:44px;
    background:linear-gradient(to bottom,var(--band-edge) 0 3px,var(--band) 3px calc(100% - 3px),var(--band-edge) calc(100% - 3px));
    opacity:.75;
  }
  .border-band.top{top:4px}
  .border-band.bottom{bottom:4px}
  .border-rule{position:absolute;left:0;width:100%;height:1px;background:var(--rule)}
  .border-rule.top{top:54px}
  .border-rule.bottom{bottom:54px}

  .brand{
    position:absolute;top:66px;left:0;width:100%;
    display:flex;align-items:center;justify-content:center;gap:14px;
  }
  .brand-dot{width:50px;height:50px;border-radius:50%;background:var(--brand-green)}
  .brand-name{
    font-family:"Arimo",sans-serif;font-size:20px;letter-spacing:2px;
    text-transform:uppercase;color:var(--brand-green);
  }

  .product-name{
    position:absolute;top:248px;left:0;width:100%;text-align:center;
    font-family:"Cinzel",serif;font-weight:900;color:var(--ink);
    font-size:84px;line-height:88px;letter-spacing:1px;
  }
  .divider{
    position:absolute;left:50%;transform:translateX(-50%);
    display:flex;align-items:center;gap:10px;
  }
  .divider .line{width:110px;height:2px;background:var(--rule)}
  .divider .knot{width:14px;height:14px;border:2px solid var(--rule);transform:rotate(45deg)}
  .divider.upper{top:461px}
  .divider.lower{top:580px}

  .product-type{
    position:absolute;top:500px;left:0;width:100%;text-align:center;
    font-family:"Arimo",sans-serif;font-size:46px;color:var(--magenta);letter-spacing:1px;
  }
  .flavor-art{
    position:absolute;top:598px;left:calc(50% - 42px);width:84px;height:70px;
    border-radius:50% 50% 45% 45%;
    background:radial-gradient(circle at 40% 40%,var(--fruit-light),var(--fruit-deep) 75%);
  }
  .flavor-name{
    position:absolute;top:668px;left:0;width:100%;text-align:center;
    font-family:"Tinos",serif;font-size:27px;color:var(--leaf);
  }
  .details{
    position:absolute;top:712px;left:0;width:100%;
    font-family:"Arimo",sans-serif;font-size:19px;color:var(--small-ink);
  }
  .details span{position:absolute;white-space:nowrap}
  .batch{left:172px}
  .volume{left:410px}
  .shake{left:700px}
  .ingredients-heading{
    position:absolute;left:14px;top:720px;transform-origin:left top;transform:rotate(-90deg);
    font-family:"Arimo",sans-serif;font-size:17px;color:var(--small-ink);
  }
</style>
</head>
<body>
<div class="canvas">
  <section class="label">
    <div class="border-band top" role="img" aria-label="Ornamental border pattern"></div>
    <div class="border-rule top"></div>

    <div class="brand">
      <span class="brand-dot"></span>
      <span class="brand-name">Stone Hollow Vinegar Works</span>
    </div>

    <h1 class="product-name">Stone Hollow<br>Shrub</h1>

    <div class="divider upper"><span class="line"></span><span class="knot"></span><span class="line"></span></div>
    <p class="product-type">COCKTAIL VINEGAR</p>
    <div class="divider lower"><span class="line"></span><span class="knot"></span><span class="line"></span></div>

    <div class="flavor-art" role="img" aria-label="Illustration of a pomegranate with seeds and leaves"></div>
    <p class="flavor-name">Pomegranate</p>

    <p class="ingredients-heading">Ingredients</p>
    <div class="details">
      <span class="batch">Batch number</span>
      <span class="volume">Vol 16.9oz/500mL</span>
      <span class="shake">Shake before using</span>
    </div>

    <div class="border-rule bottom"></div>
    <div class="border-band bottom" role="img" aria-label="Ornamental border pattern"></div>
  </section>
</div>
</body>
</html>
```